Business Card

We need a business card for a fundraising/sales and marketing company called Kelvora Appeals services. The logo colours are Red Black and white. The final design should communicate professional, reliable yet fun and charity minded
Updates

Sorry for the delay. A decision will be made in the next 48 hours. we are stuck between two designs. Kind Regards, Molly Ravenscroft

Industry/Entity Type

Marketing

```html
<!DOCTYPE html>
<html lang="en">
<head>
<meta charset="utf-8">
<title>Kelvora Appeals services – Business Card</title>
<link href="https://fonts.googleapis.com/css2?family=Open+Sans:wght@400;600&display=swap" rel="stylesheet">
<style>
  :root {
    --brand-red: #e31b23;
    --ink-dark: #3a3a3a;
    --ink-grey: #555555;
    --wave-grey: #4a4a4a;
    --card-white: #ffffff;
    --backdrop: #e8e8e8;
  }
  html, body {
    margin: 0;
    width: 1200px;
    height: 873px;
    overflow: hidden;
    background: var(--backdrop);
    font-family: "Open Sans", Arial, sans-serif;
  }
  .canvas {
    position: relative;
    width: 1200px;
    height: 873px;
  }
  .card {
    position: absolute;
    top: 288px;
    width: 520px;
    height: 297px;
    background: var(--card-white);
    box-shadow: 0 2px 10px rgba(0,0,0,0.15);
    overflow: hidden;
  }
  .card--front { left: 60px; }
  .card--back { left: 620px; }
  .card__wave {
    position: absolute;
    inset: 0;
    width: 100%;
    height: 100%;
  }
  .card__web {
    position: absolute;
    left: 20px;
    bottom: 22px;
    color: var(--card-white);
    font-size: 12px;
    font-weight: 600;
  }
  .brand {
    position: absolute;
    display: flex;
    align-items: center;
    gap: 8px;
    color: var(--ink-dark);
    font-weight: 400;
    white-space: nowrap;
  }
  .brand__dot {
    border-radius: 50%;
    background: var(--brand-red);
  }
  .card--front .brand { left: 250px; top: 34px; font-size: 22px; }
  .card--front .brand__dot { width: 14px; height: 14px; }
  .card--back .brand { left: 140px; top: 64px; font-size: 36px; }
  .card--back .brand__dot { width: 22px; height: 22px; }
  .holder {
    position: absolute;
    left: 36px;
    top: 34px;
  }
  .holder__name {
    margin: 0;
    font-size: 20px;
    font-weight: 400;
    color: var(--ink-dark);
    letter-spacing: 0.5px;
  }
  .holder__role {
    margin: 0;
    font-size: 11px;
    font-weight: 600;
    color: var(--brand-red);
  }
  .contacts {
    position: absolute;
    left: 250px;
    top: 100px;
    margin: 0;
    padding: 0;
    list-style: none;
    font-size: 12px;
    color: var(--ink-grey);
  }
  .contacts li {
    display: flex;
    align-items: center;
    gap: 8px;
    height: 18px;
  }
  .contacts svg {
    width: 12px;
    height: 12px;
    fill: var(--brand-red);
  }
</style>
</head>
<body>
<main class="canvas">

  <section class="card card--front" aria-label="Business card front">
    <svg class="card__wave" viewBox="0 0 520 297" preserveAspectRatio="none" aria-hidden="true">
      <path d="M0,190 C140,198 240,282 420,297 L0,297 Z" fill="var(--brand-red)"/>
      <path d="M0,172 C150,178 260,282 520,284" fill="none" stroke="var(--wave-grey)" stroke-width="6"/>
    </svg>
    <div class="holder">
      <p class="holder__name">YOUR NAME</p>
      <p class="holder__role">President</p>
    </div>
    <div class="brand"><span class="brand__dot"></span>Kelvora Appeals</div>
    <ul class="contacts">
      <li><svg viewBox="0 0 12 12"><path d="M6 1 L11 6 H9.5 V11 H7 V8 H5 V11 H2.5 V6 H1 Z"/></svg>Street No. 23 Harlow</li>
      <li><svg viewBox="0 0 12 12"><path d="M2 1 H5 L6 4 L4.5 5 C5.2 6.6 5.6 7 7 7.5 L8 6 L11 7 V10 C11 10.6 10.6 11 10 11 C5 11 1 7 1 2 C1 1.4 1.4 1 2 1 Z"/></svg>+123.456.789</li>
      <li><svg viewBox="0 0 12 12"><path d="M3.5 0.5 H8.5 V11.5 H3.5 Z M4.5 1.5 V9.5 H7.5 V1.5 Z"/></svg>+123.456.789</li>
      <li><svg viewBox="0 0 12 12"><path d="M1 2.5 H11 V9.5 H1 Z M1.8 3.2 L6 6.5 L10.2 3.2 V3 H1.8 Z"/></svg>username@kelvoraappeals.com</li>
    </ul>
    <span class="card__web">www.kelvoraappeals.com</span>
  </section>

  <section class="card card--back" aria-label="Business card back">
    <svg class="card__wave" viewBox="0 0 520 297" preserveAspectRatio="none" aria-hidden="true">
      <path d="M0,190 C140,198 240,282 420,297 L0,297 Z" fill="var(--brand-red)"/>
      <path d="M0,172 C150,178 260,282 520,284" fill="none" stroke="var(--wave-grey)" stroke-width="6"/>
    </svg>
    <div class="brand"><span class="brand__dot"></span>Kelvora Appeals</div>
    <span class="card__web">www.kelvoraappeals.com</span>
  </section>

</main>
</body>
</html>
```